Web Design Project

site will be : www.quickchatrelay.com
We are a new business specialising in providing online customer support and sales services for a wide range of business types.

Will have to source suitable stock shots for images.
will also souce sample graphics of service, to follow.
Updates

Project Deadline Extended
Reason: This should allow enough time for any outstanding designs to be submitted. We are keen to press on so Further extension will only be considered if the designer contacts me with a very good reason.

Target Market(s)

Online Businesses

Industry/Entity Type

Business

Requirements
Must have
• Live Help Button....see briefing document for further details

```html
<!DOCTYPE html>
<html lang="en">
<head>
<meta charset="utf-8">
<title>Quick Chat Relay – Services</title>
<link rel="stylesheet" href="https://fonts.googleapis.com/css2?family=Source+Sans+3:ital,wght@0,400;0,600;0,700;1,700&family=Arimo&display=swap">
<style>
  :root {
    --blue-deep: #1f63c4;
    --blue-text: #2b63a8;
    --sky-top: #9fcaf5;
    --sky-mid: #d6e9fb;
    --orange: #f0a81c;
    --orange-light: #f7c24a;
    --orange-pale: #fbd98a;
    --grey-text: #555a60;
    --nav-text: #3a3f44;
    --rule: #d9d9d9;
    --brace: #cfcfcf;
    --white: #ffffff;
  }
  * { box-sizing: border-box; margin: 0; padding: 0; }
  html, body { width: 1200px; height: 717px; overflow: hidden; background: var(--white); }
  body { font-family: "Source Sans 3", sans-serif; position: relative; }

  .hero-band {
    position: absolute; left: 0; top: 0; width: 1200px; height: 340px;
    background: linear-gradient(180deg, var(--white) 0px, var(--sky-top) 95px, var(--sky-mid) 230px, var(--white) 335px);
  }
  .hero-glow {
    position: absolute; left: 490px; top: 60px; width: 560px; height: 250px; border-radius: 50%;
    background: radial-gradient(ellipse at center, rgba(255,255,255,0.35), rgba(255,255,255,0) 70%);
  }

  .brand { position: absolute; left: 138px; top: 16px; display: flex; align-items: center; gap: 8px; }
  .brand-mark { width: 12px; height: 12px; background: var(--orange); }
  .brand-name {
    font-size: 19px; font-weight: 600; color: var(--blue-deep); letter-spacing: 0.5px;
    line-height: 20px; width: 110px;
  }

  .main-nav { position: absolute; left: 300px; top: 26px; height: 26px; }
  .nav-item {
    position: absolute; top: 0; height: 26px; line-height: 26px; font-size: 11px; font-weight: 600;
    color: var(--nav-text); white-space: nowrap; padding-left: 14px;
  }
  .nav-item::before { content: "→"; position: absolute; left: 0; font-size: 8px; }
  .nav-item.is-active {
    background: var(--blue-deep); color: var(--white); border-radius: 5px; padding: 0 10px 0 20px; width: 71px;
  }
  .nav-item.is-active::before { left: 7px; }

  .agent-badge {
    position: absolute; left: 785px; top: -70px; width: 250px; height: 130px; border-radius: 50%;
    background: radial-gradient(ellipse at 50% 35%, var(--orange) 0%, var(--orange-light) 55%, var(--orange-pale) 100%);
  }
  .agent-status { position: absolute; left: 863px; top: 7px; font-size: 12px; color: var(--white); }
  .agent-status strong { font-weight: 700; }
  .agent-link { position: absolute; left: 865px; top: 27px; font-size: 11px; color: #2f7d12; display: flex; align-items: center; gap: 5px; }
  .agent-link .dot { width: 11px; height: 11px; border-radius: 50%; background: #3f8f1c; }
  .agent-link strong { font-weight: 700; }

  .hero-photo {
    position: absolute; left: 690px; top: 64px; width: 260px; height: 226px;
    background: radial-gradient(ellipse at 55% 45%, #f1d2c2 0%, #d9b3a1 35%, rgba(200,220,240,0) 75%);
  }

  .hero-title { position: absolute; left: 154px; top: 98px; font-size: 36px; color: var(--white); font-weight: 400; }
  .hero-points { position: absolute; left: 274px; top: 156px; list-style: none; }
  .hero-points li {
    display: flex; align-items: center; height: 31px; font-size: 16px; color: var(--blue-text);
  }
  .hero-points li::before {
    content: "›"; width: 15px; height: 15px; border-radius: 50%; background: var(--orange);
    color: #8a5a00; font-size: 11px; line-height: 14px; text-align: center; margin-right: 20px; font-weight: 700;
  }
  .hero-points strong { font-weight: 700; margin: 0 4px; }

  .cta-button {
    position: absolute; left: 175px; top: 239px; width: 490px; height: 43px; border-radius: 6px;
    background: linear-gradient(180deg, var(--orange-light), var(--orange));
    color: var(--white); font-size: 18px; line-height: 43px; padding-left: 19px; white-space: nowrap;
  }
  .cta-button strong { font-weight: 700; }

  .benefits-heading { position: absolute; left: 155px; top: 327px; font-size: 14px; color: var(--nav-text); }
  .benefits-heading span { text-decoration: underline; }

  .benefit { position: absolute; display: flex; align-items: center; font-size: 14px; color: var(--grey-text); white-space: nowrap; }
  .benefit-num {
    width: 26px; height: 26px; border-radius: 50%; margin-right: 14px;
    background: radial-gradient(circle at 40% 35%, #4d8fd6, #1d4f96);
    color: var(--white); font-size: 16px; font-weight: 700; font-style: italic; text-align: center; line-height: 26px;
  }

  .brace { position: absolute; left: 965px; top: 360px; }

  .footer-rule { position: absolute; left: 138px; top: 503px; width: 912px; height: 1px; background: var(--rule); }
  .footer-note { position: absolute; top: 514px; font-family: "Arimo", sans-serif; font-size: 8.5px; color: #6a6a6a; white-space: nowrap; }
</style>
</head>
<body>
  <div class="hero-band"></div>
  <div class="hero-glow"></div>

  <div class="brand">
    <span class="brand-mark"></span>
    <span class="brand-name">QUICK CHAT RELAY</span>
  </div>

  <nav class="main-nav">
    <span class="nav-item" style="left:3px">HOME</span>
    <span class="nav-item is-active" style="left:73px">SERVICES</span>
    <span class="nav-item" style="left:165px">ABOUT US</span>
    <span class="nav-item" style="left:260px">FAQ</span>
    <span class="nav-item" style="left:326px">PRICING</span>
    <span class="nav-item" style="left:412px">CONTACT US</span>
  </nav>

  <div class="agent-badge"></div>
  <div class="agent-status">Agent <strong>Online Now</strong></div>
  <div class="agent-link"><span class="dot"></span>Click for <strong>Live Help</strong></div>

  <div class="hero-photo" role="img" aria-label="Smiling support agent wearing a headset"></div>

  <h1 class="hero-title">Do you</h1>
  <ul class="hero-points">
    <li>Need to close<strong>more</strong>online sales ?</li>
    <li>Want to<strong>improve</strong>your customer support ?</li>
  </ul>

  <div class="cta-button">GET <strong>LIVE CHAT CUSTOMER HELP</strong> ON YOUR WEBSITE TODAY !</div>

  <p class="benefits-heading"><span>Quick Chat Relay will</span> :</p>

  <div class="benefit" style="left:157px;top:360px"><span class="benefit-num">1</span>Convert visitors to your website into customers</div>
  <div class="benefit" style="left:157px;top:403px"><span class="benefit-num">2</span>Improve Customer Communication</div>
  <div class="benefit" style="left:157px;top:446px"><span class="benefit-num">3</span>Monitor visitors to your website in real time</div>
  <div class="benefit" style="left:545px;top:360px"><span class="benefit-num">4</span>Work closely with you to identify your support requirements</div>
  <div class="benefit" style="left:545px;top:403px"><span class="benefit-num">5</span>Provide professional agents to implement those requirements</div>
  <div class="benefit" style="left:545px;top:445px"><span class="benefit-num">6</span>Reduce your operational costs</div>

  <svg class="brace" width="40" height="122" viewBox="0 0 40 122" aria-hidden="true">
    <path d="M6 4 C22 4 22 12 22 30 L22 46 C22 56 26 60 34 61 C26 62 22 66 22 76 L22 92 C22 110 22 118 6 118"
          fill="none" stroke="var(--brace)" stroke-width="7" stroke-linecap="round"/>
  </svg>

  <div class="footer-rule"></div>
  <p class="footer-note" style="left:158px">Based in Ireland with European agents to cater for a&nbsp; European market......WE CAN BRING YOUR WEBSITE TO LIFE.....</p>
  <p class="footer-note" style="left:881px">Copyright © 2011 Quick Chat Relay.</p>
</body>
</html>
```